BRAMLEIGH real estate family office

Hello, Our business is a real estate intermediation activity on high-end goods (amounts exceeding € 10m) for corporate and private clients. You can see our logo on the site www.bramleigh-invented.fr We would like to keep that spirit with the hexagon that represents France (transactions between Monaco and Saint Tropez, Courchevel and Paris). And the "baseline" that is "real estate family office". The corporate logo should be and can be printed by embossing (relief). We must integrate the name, first name, phone, email and website. Finally, to imbibe the spirit of business, here is a detail of the activity. "Genuine consulting firm in real estate investments, BRAMLEIGH works with its customers as a specialized player in the high-end markets, we are recognized for our ultra-confidential approach and tailor-made, as well as the quality of our network. We broadcast any information on the market and we work exclusively through a strong relationship we have developed over the years. BRAMLEIGH is active on the French Riviera (from Monaco to Saint-Tropez), the Alps (Courchevel, Méribel, Megève) and Paris (essentially market premium). Always looking for opportunities for our clients, we work on two investment areas: residential luxury real estate (properties, vineyards, mansions, land, etc.) commercial real estate (empty office buildings or yield, hotel properties, land, etc.) "

Target Market(s)

High foreign end customers. corporate and private.

Industry/Entity Type

Real Estate

Contact Information for Business Card

LOGO
baseline
Laurent Dufossé
+33(0)6.41.57.09.64
ld@bramleigh-invented.fr
www.bramleigh-invented.fr

Font styles to use
Serif

Colors
cedeed
0255a3
3277b5
85abd2
85cae6
34a7d7
0792cd
cfdeed
1b1b1b

Requirements
Must have
• see description

```html
<!DOCTYPE html>
<html lang="fr">
<head>
<meta charset="utf-8">
<title>Bramleigh – carte de visite</title>
<link rel="stylesheet" href="https://fonts.googleapis.com/css2?family=Open+Sans:wght@400;700&display=swap">
<style>
  :root {
    --page: #dedcdc;
    --card-top: #f2f0f0;
    --brand-blue: #0a3a8f;
    --band-blue: #053891;
    --white: #ffffff;
  }
  * { margin: 0; padding: 0; box-sizing: border-box; }
  html, body {
    width: 1200px;
    height: 900px;
    overflow: hidden;
    background: var(--page);
  }
  .business-card {
    position: absolute;
    left: 150px;
    top: 172px;
    width: 900px;
    height: 555px;
    background: var(--card-top);
    box-shadow: 0 10px 30px rgba(0, 0, 0, 0.15);
    overflow: hidden;
  }
  .brand-area {
    height: 302px;
    display: flex;
    align-items: center;
    justify-content: center;
    padding-top: 14px;
  }
  .brand-lockup {
    display: inline-flex;
    flex-direction: column;
    align-items: flex-end;
  }
  .brand-row {
    display: flex;
    align-items: center;
  }
  .brand-mark {
    width: 62px;
    height: 62px;
    background: var(--brand-blue);
    margin-right: 24px;
  }
  .brand-name {
    font-family: "Open Sans", sans-serif;
    font-weight: 700;
    font-size: 78px;
    line-height: 1;
    letter-spacing: 4px;
    color: var(--brand-blue);
  }
  .brand-baseline {
    font-family: "Open Sans", sans-serif;
    font-weight: 400;
    font-size: 26px;
    letter-spacing: 1.5px;
    color: var(--brand-blue);
    margin-top: 8px;
    margin-right: 6px;
  }
  .contact-band {
    position: absolute;
    left: 0;
    bottom: 0;
    width: 100%;
    height: 253px;
    background: var(--band-blue);
    color: var(--white);
    font-family: "Open Sans", sans-serif;
  }
  .holder-name {
    position: absolute;
    left: 118px;
    top: 102px;
    font-size: 28px;
    font-weight: 700;
    letter-spacing: -0.3px;
  }
  .contact-list {
    position: absolute;
    left: 447px;
    top: 76px;
    list-style: none;
  }
  .contact-item {
    display: flex;
    align-items: center;
    height: 32px;
    font-size: 23px;
  }
  .contact-icon {
    width: 18px;
    height: 18px;
    margin-right: 18px;
    fill: var(--white);
    flex-shrink: 0;
  }
</style>
</head>
<body>
  <article class="business-card">
    <header class="brand-area">
      <div class="brand-lockup">
        <div class="brand-row">
          <span class="brand-mark" aria-hidden="true"></span>
          <span class="brand-name">BRAMLEIGH</span>
        </div>
        <span class="brand-baseline">real estate family office</span>
      </div>
    </header>
    <section class="contact-band">
      <p class="holder-name">Laurent Dufossé</p>
      <ul class="contact-list">
        <li class="contact-item">
          <svg class="contact-icon" viewBox="0 0 24 24" aria-hidden="true"><path d="M6.6 10.8a15.1 15.1 0 0 0 6.6 6.6l2.2-2.2a1 1 0 0 1 1-.25 11.4 11.4 0 0 0 3.6.57 1 1 0 0 1 1 1V20a1 1 0 0 1-1 1A17 17 0 0 1 3 4a1 1 0 0 1 1-1h3.5a1 1 0 0 1 1 1c0 1.250.2 2.45.57 3.57a1 1 0 0 1-.25 1z"/></svg>
          <span>+33(0)6.41.57.09.64</span>
        </li>
        <li class="contact-item">
          <svg class="contact-icon" viewBox="0 0 24 24" aria-hidden="true"><path d="M3 7.2V18h18V7.2l-9 6.8z M3.6 6h16.8L12 12.4z"/></svg>
          <span>ld@bramleigh-invented.fr</span>
        </li>
        <li class="contact-item">
          <svg class="contact-icon" viewBox="0 0 24 24" aria-hidden="true"><path d="M12 2a10 10 0 1 0 0 20 10 10 0 0 0 0-20zm-1 17.9A8 8 0 0 1 4.2 10.2L9 15v1a2 2 0 0 0 2 2zm6.9-2.5A2 2 0 0 0 16 16h-1v-3a1 1 0 0 0-1-1H8v-2h2a1 1 0 0 0 1-1V7h2a2 2 0 0 0 2-2v-.4a8 8 0 0 1 2.9 12.8z"/></svg>
          <span>www.bramleigh-invented.fr</span>
        </li>
      </ul>
    </section>
  </article>
</body>
</html>
```